Webdesign für  Kranken- und Seniorenpflege
Webdesign für Kranken- und Seniorenpflege
Zielgruppe
Ambulante Kranken- und Seniorenpflege
Tagespflege in Limbach-Oberfrohna, Mittweida und Chemnitz
Palliativpflege
Aufgabenstellung
- Erstellung in Adobe Photoshop
- Orientieren Sie sich am Socialmedia-Auftritt des Kunden

```html
<!DOCTYPE html>
<html lang="de">
<head>
<meta charset="utf-8">
<title>Pflegehafen – Kranken- und Seniorenpflege</title>
<link href="https://fonts.googleapis.com/css2?family=Lexend+Deca:wght@400;500;600&family=Lato:wght@400;700&display=swap" rel="stylesheet">
<style>
:root{
  --maroon:#9b0f3f;
  --pink:#fde6ed;
  --bg:#f5f5f5;
  --white:#ffffff;
  --yellow:#fbbf24;
  --text:#2b2b2b;
  --muted:#6b6b6b;
}
*{box-sizing:border-box;margin:0;padding:0}
html,body{width:1200px;height:3294px;overflow:hidden}
body{position:relative;background:var(--bg);font-family:"Lato",sans-serif;color:var(--text)}
.abs{position:absolute}

/* header */
.site-header{left:0;top:0;width:1200px;height:82px;background:var(--white)}
.brand{left:98px;top:14px;display:flex;align-items:center;gap:10px;font-family:"Lexend Deca",sans-serif;font-weight:600;font-size:22px;color:var(--maroon)}
.brand-dot{width:46px;height:46px;border-radius:50%;background:var(--yellow)}
.social{display:flex;gap:14px}
.social span{width:22px;height:22px;border-radius:50%;border:2.5px solid var(--maroon)}
.header-social{left:1045px;top:30px}
.main-nav{left:0;top:82px;width:1200px;height:33px;background:var(--maroon);display:flex;align-items:center;justify-content:space-between;padding:0 92px 0 93px;font-size:11.5px;color:var(--white)}
.main-nav .active{font-weight:700}

/* hero */
.hero{left:0;top:115px;width:1200px;height:525px;background:linear-gradient(120deg,#6d7f4e 0%,#a8a77a 22%,#2f5f9c 45%,#d9c6b6 70%,#e8ebef 100%)}
.hero-wave{left:0;top:115px}
.hero-dots{left:185px;top:396px;display:flex;gap:8px}
.hero-dots span{width:20px;height:2px;background:rgba(255,255,255,.7)}
.hero-dots span:first-child{background:#fff}
.hero-title{left:185px;top:410px;font-family:"Lexend Deca",sans-serif;font-weight:600;font-size:34px;line-height:47px;color:var(--white)}
.btn{display:flex;align-items:center;justify-content:center;border-radius:4px;font-family:"Lexend Deca",sans-serif;font-size:12px;font-weight:500;color:var(--white);background:var(--maroon);text-decoration:none}
.hero-btn{left:186px;top:518px;width:143px;height:32px}

/* section heads */
.eyebrow{width:1200px;left:0;text-align:center;font-family:"Lexend Deca",sans-serif;font-size:13px;color:var(--muted)}
.sec-title{width:1200px;left:0;text-align:center;font-family:"Lexend Deca",sans-serif;font-weight:600;font-size:29px;line-height:36px;color:var(--maroon)}
.rule{width:20px;height:2px;background:var(--text)}

/* services */
.services{left:179px;top:813px;display:flex;gap:12px}
.service-card{width:201px;height:226px;background:var(--white);border-radius:6px;padding:8px;text-align:center}
.service-photo{height:135px;border-radius:2px 2px 70px 2px}
.service-card h3{margin-top:24px;font-family:"Lexend Deca",sans-serif;font-weight:500;font-size:16px;line-height:23px;color:var(--maroon)}

/* jobs */
.jobs-blob{left:0;top:1132px}
.jobs-photo{left:180px;top:1281px;width:455px;height:319px;border-radius:4px;background:linear-gradient(135deg,#c9ccd0,#3e4756 50%,#d7c8b8);box-shadow:0 10px 24px rgba(0,0,0,.18)}
.jobs-label{left:700px;top:1303px;font-family:"Lexend Deca",sans-serif;font-size:13px;color:var(--muted)}
.jobs-title{left:700px;top:1325px;font-family:"Lexend Deca",sans-serif;font-weight:600;font-size:29px;color:var(--maroon)}
.jobs-rule{left:700px;top:1368px}
.jobs-text{left:700px;top:1390px;width:318px;font-size:13px;line-height:20px}
.jobs-btn{left:700px;top:1548px;width:143px;height:32px}

/* news */
.news-list{left:266px;top:1916px}
.news-item{display:flex;gap:26px;height:182px}
.news-photo{width:218px;height:141px;border-radius:3px;flex:none}
.tag{display:inline-block;background:var(--maroon);color:var(--white);font-family:"Lexend Deca",sans-serif;font-size:10px;padding:5px 10px;border-radius:3px}
.news-body h3{margin-top:12px;font-family:"Lexend Deca",sans-serif;font-weight:500;font-size:17px;color:var(--text)}
.news-body p{margin-top:14px;width:420px;font-size:13px;line-height:20px;color:#444}

/* cta */
.cta-wave{left:0;top:2667px}
.cta-title{left:181px;top:2795px;font-family:"Lexend Deca",sans-serif;font-weight:600;font-size:22px;color:var(--white)}
.cta-text{left:181px;top:2838px;width:455px;font-size:10.5px;line-height:20px;color:var(--white)}
.cta-phone{right:181px;top:2794px;display:flex;align-items:center;gap:10px;font-family:"Lexend Deca",sans-serif;font-weight:600;font-size:23px;color:var(--white)}
.cta-note{right:181px;top:2832px;font-size:10.5px;color:var(--white)}
.cta-btn{left:878px;top:2861px;width:142px;height:36px;background:var(--yellow);color:var(--maroon)}

/* footer */
.site-footer{left:0;top:2974px;width:1200px;height:262px;background:var(--white)}
.footer-brand{left:184px;top:3030px}
.footer-phone{left:181px;top:3096px;display:flex;align-items:center;gap:10px;font-family:"Lexend Deca",sans-serif;font-size:19px}
.footer-note{left:179px;top:3130px;font-size:11px}
.footer-social{left:182px;top:3160px}
.footer-social span{border-color:var(--text)}
.footer-col h4{font-family:"Lexend Deca",sans-serif;font-weight:500;font-size:12px;letter-spacing:.5px;margin-bottom:20px}
.footer-col a{display:block;font-size:13px;color:var(--muted);text-decoration:none;margin-bottom:10px}
.col-service{left:544px;top:3028px}
.col-company{left:836px;top:3028px}
.copyright{left:0;top:3236px;width:1200px;height:58px;background:#ececec;padding:24px 0 0 135px;font-size:11.5px;color:var(--muted)}
</style>
</head>
<body>

<header class="abs site-header">
  <div class="abs brand"><span class="brand-dot"></span>Pflegehafen</div>
  <div class="abs social header-social" aria-label="Soziale Netzwerke"><span></span><span></span></div>
</header>
<nav class="abs main-nav">
  <span class="active">Kranken- und Seniorenpflege</span>
  <span>Tagespflege</span><span>Palliativpflege</span><span>Standorte</span>
  <span>Stellenangebote</span><span>Aktuelles</span><span>Impressum / Datenschutz</span>
</nav>

<section>
  <div class="abs hero" role="img" aria-label="Foto: lächelnde Pflegekraft in blauer Kleidung mit einer älteren Dame im Freien"></div>
  <svg class="abs hero-wave" width="1200" height="525" viewBox="0 0 1200 525">
    <path d="M0,440 C130,480 230,525 380,525 C520,525 900,470 1080,445 C1170,430 1200,380 1200,340 L1200,525 L0,525 Z" fill="#f5f5f5"/>
  </svg>
  <div class="abs hero-dots"><span></span><span></span><span></span><span></span></div>
  <h1 class="abs hero-title">Herzlich Willkommen bei<br>Pflegehafen!</h1>
  <a class="abs btn hero-btn">Mehr enfahren</a>
</section>

<section>
  <p class="abs eyebrow" style="top:684px">Leistungen</p>
  <h2 class="abs sec-title" style="top:709px">Jeder verdient unsere<br>Beste Dienstleistungen</h2>
  <div class="abs rule" style="left:590px;top:783px"></div>
  <div class="abs services">
    <article class="service-card"><div class="service-photo" role="img" aria-label="Foto: Pflegerin mit Seniorin" style="background:linear-gradient(135deg,#c8b8a8,#7a2a3a 55%,#e6d3c0)"></div><h3>Kranken- und<br>Seniorenpflege</h3></article>
    <article class="service-card"><div class="service-photo" role="img" aria-label="Foto: Senioren beim Spielen am Tisch" style="background:linear-gradient(135deg,#9a8676,#d9b79a 55%,#c9a08c)"></div><h3>Tagespflege</h3></article>
    <article class="service-card"><div class="service-photo" role="img" aria-label="Foto: Seniorin im Gespräch mit Ärztin" style="background:linear-gradient(135deg,#8aa2c4,#c7cfd9 55%,#f2f0ee)"></div><h3>Palliativpflege</h3></article>
    <article class="service-card"><div class="service-photo" role="img" aria-label="Foto: Pflegerin am Bett einer Patientin" style="background:linear-gradient(135deg,#7a2a3a,#b3a594 50%,#e5e3df)"></div><h3>Pflegeberatung</h3></article>
  </div>
</section>

<section>
  <svg class="abs jobs-blob" width="1200" height="614" viewBox="0 0 1200 614">
    <path d="M0,150 C0,110 40,80 100,72 L880,8 C960,-8 1030,0 1200,95 L1200,430 C1190,515 1130,535 1070,540 L460,606 C390,614 330,608 270,594 L0,525 Z" fill="#fde6ed"/>
  </svg>
  <div class="abs jobs-photo" role="img" aria-label="Foto: fünf lächelnde Teammitglieder im Büro"></div>
  <p class="abs jobs-label">Stellenangebote</p>
  <h2 class="abs jobs-title">wir suchen dich!</h2>
  <div class="abs rule jobs-rule"></div>
  <p class="abs jobs-text">Als Pflegefachkraft (m/w/d) liebst du es, mit Menschen zu arbeiten und hast das Herz am rechten Fleck? Toll, dann suchen wir Dich!<br>Du suchst auch gerade nach einer neuen Herausforderung, um Dich persönlich weiterzuentwickeln? Wenn ja, dann wollen wir Dich kennenlernen.</p>
  <a class="abs btn jobs-btn">Jetzt Bewerben</a>
</section>

<section>
  <p class="abs eyebrow" style="top:1810px">Aktualles</p>
  <h2 class="abs sec-title" style="top:1835px">Neuesten Nachrichten</h2>
  <div class="abs rule" style="left:590px;top:1875px"></div>
  <div class="abs news-list">
    <article class="news-item"><div class="news-photo" role="img" aria-label="Foto: Brettspiel auf einem Tisch" style="background:linear-gradient(135deg,#f0ece8,#d4a86a 50%,#e8e4e0)"></div>
      <div class="news-body"><span class="tag">Aktualles</span><h3>Sommerfest in der Tagespflege „Sonnenhof“</h3><p>Sommereinklang in der Tagespflege „Sonnenhof“ in Chemnitz. Bei sommerlichen Temperaturen und strahlenden Sonnenschein verweilten die Tagesgäste auf unserer großzügigen Terrasse. Unsere Betreuungskraft Karla sorgte für …</p></div></article>
    <article class="news-item"><div class="news-photo" role="img" aria-label="Foto: Seniorin im Gespräch" style="background:linear-gradient(135deg,#8aa2c4,#c7cfd9 55%,#f2f0ee)"></div>
      <div class="news-body"><span class="tag">Aktualles</span><h3>Wochenausklang am Schwanenteich in Mittweida</h3><p>Die vergangene Woche haben wir mit unseren Gästen aus der Tagespflege „Mühlentor“ am Schwanenteich in Mittweida ausklingen lassen. Nach einem Spaziergang durch den Park …</p></div></article>
    <article class="news-item"><div class="news-photo" role="img" aria-label="Foto: Senioren beim Spielen" style="background:linear-gradient(135deg,#9a8676,#d9b79a 55%,#c9a08c)"></div>
      <div class="news-body"><span class="tag">Aktualles</span><h3>Maifest in der Tagespflege „Mühlentor“</h3><p>Zu unserem Maifest in der Tagespflege „Mühlentor“ in Mittweida erlebten unsere Gäste bei schönstem Wetter einen abwechslungsreichen Tag. Mit leckerer Maibowle, Nudelsalat und Bratwurst …</p></div></article>
    <article class="news-item"><div class="news-photo" role="img" aria-label="Foto: Pflegerinnen beim Basteln zu Ostern" style="background:linear-gradient(135deg,#7a2a3a,#b08a7a 50%,#8aa34a)"></div>
      <div class="news-body"><span class="tag">Aktualles</span><h3>Ostern in unserer Tagespflege „Lindenhof“</h3><p>Das Osterfest in unserer Tagespflege „Lindenhof“ in Limbach-Oberfrohna war wieder ein gelungenes Fest. Traditionell gab es für unsere Gäste ein leckeres „Osterlamm“ und natürlich …</p></div></article>
  </div>
</section>

<section>
  <svg class="abs cta-wave" width="1200" height="307" viewBox="0 0 1200 307">
    <path d="M0,40 L1040,55 C1150,55 1185,30 1200,0 L1200,307 L0,307 Z" fill="#9b0f3f"/>
  </svg>
  <h2 class="abs cta-title">Planen Sie Ihren Service noch heute</h2>
  <p class="abs cta-text">Lorem ipsum dolor sit amet, consectetur adipiscing elit. Faucibus sodales et sit egestas tellus venenatis pulvinar. Fermentum nullam morbi vitae lacus sed ullamcorper in leo sit. Ultricies ac enim quam venenatis nibh amet</p>
  <div class="abs cta-phone"><svg width="20" height="20" viewBox="0 0 24 24"><path d="M6.6 10.8a15 15 0 0 0 6.6 6.6l2.2-2.2a1 1 0 0 1 1-.25 11.4 11.4 0 0 0 3.6.57 1 1 0 0 1 1 1V20a1 1 0 0 1-1 1A17 17 0 0 1 3 4a1 1 0 0 1 1-1h3.5a1 1 0 0 1 1 1c0 1.25.2 2.45.57 3.57a1 1 0 0 1-.25 1z" fill="#fff"/></svg>0800 3127590</div>
  <p class="abs cta-note">die kostenfreie präsent darstellen</p>
  <a class="abs btn cta-btn">Jetzt registrieren</a>
</section>

<footer class="abs site-footer"></footer>
<div class="abs brand footer-brand"><span class="brand-dot"></span>Pflegehafen</div>
<div class="abs footer-phone"><svg width="16" height="16" viewBox="0 0 24 24"><path d="M6.6 10.8a15 15 0 0 0 6.6 6.6l2.2-2.2a1 1 0 0 1 1-.25 11.4 11.4 0 0 0 3.6.57 1 1 0 0 1 1 1V20a1 1 0 0 1-1 1A17 17 0 0 1 3 4a1 1 0 0 1 1-1h3.5a1 1 0 0 1 1 1c0 1.25.2 2.45.57 3.57a1 1 0 0 1-.25 1z" fill="#2b2b2b"/></svg>0800 3127590</div>
<p class="abs footer-note">die kostenfreie präsent darstellen</p>
<div class="abs social footer-social" aria-label="Soziale Netzwerke"><span></span><span></span></div>
<div class="abs footer-col col-service"><h4>SERVICE</h4><a>Kranken- und Seniorenpflege</a><a>Tagespflege</a><a>Pflegeberatung</a></div>
<div class="abs footer-col col-company"><h4>UNTERNEHMEN</h4><a>Cookie-Einstellungen</a><a>Impressum</a><a>AGB</a><a>Datenschutz</a></div>
<div class="abs copyright">© 2022 - pflegehafen-sachsen.de</div>

</body>
</html>
```